1. Can you describe what your company does?
-> We at M and P Orbex, we do Tube bending and its subassemblies. We can cater to different materials like Mild Steel, Stainless Steel, Aluminium and other non-ferrous material. We collaborate with our clients to make precise components to meet their industry requirements. At M&P Orbex we cater to smaller batches or high-volume requirements as per project needs.

2. Who are your target customers for the website?
-> Automotive, Road construction, warehouse equipment, Data centers, beverage equipment industry, electronics products manufacturers for making fixtures.
-> customers which require tubes and pipe bending, exhaust pipes, sheet metal parts

3. Do you have an existing domain name / website address?
-> This was an existing site: https://www.mandporbex.co.in/industry
-> using design.com I created this: https://sitelaunch.web/MandPOrbexpvtltd
But I am not very satisfied with the one I have created using design.com

4. In addition to a Home Page, which other pages / sections would you like your website to have:
About Us
Contact Us
Products / Services
Office / Mailing Address
Terms and Conditions

For each of the pages / sections you’d like to have, please provide the text (and images, if available) you would like to include.
-> Can you use the content that I have added on design.com : https://sitelaunch.web/MandPOrbexpvtltd

5. Which of the below are features and functionalities your website will need:
Image Gallery
Videos
Contact Form

6. Please provide the URLs for the social media profiles you'd like to link to the website.
-> Don't have one yet.

Coding

Coded - Design and coding required

```html
<!DOCTYPE html>
<html lang="en">
<head>
<meta charset="utf-8">
<title>M and P Orbex – Tube Bending</title>
<link href="https://fonts.googleapis.com/css2?family=Josefin+Sans:wght@400;600;700&family=Roboto:wght@400;500;700;900&display=swap" rel="stylesheet">
<style>
:root{
  --blue:#24449c;
  --grey:#808080;
  --ghost:#eef0f5;
  --ghost-blue:#d4dcee;
  --pale:#e1e9f8;
  --text:#3d3d3d;
  --dark:#4e4e4e;
  --white:#ffffff;
}
*{margin:0;padding:0;box-sizing:border-box}
html,body{width:1200px;height:4563px;overflow:hidden;background:var(--white);font-family:'Roboto',sans-serif;color:var(--text)}
.page{position:relative;width:1200px;height:4563px;overflow:hidden}
.abs{position:absolute}
.btn{position:absolute;display:flex;align-items:center;justify-content:center;background:var(--blue);color:var(--white);font:700 15px 'Roboto',sans-serif;border-radius:30px;text-transform:uppercase;letter-spacing:.2px}
.photo{position:absolute}
.topbar-left{left:0;top:0;width:502px;height:57px;background:#8a8a8a;border-bottom-right-radius:40px}
.topbar-right{left:502px;top:0;width:698px;height:57px;background:var(--blue);border-bottom-left-radius:40px;color:var(--white);font-size:16px;display:flex;align-items:center;gap:10px;padding-left:60px}
.topbar-right .ico{width:30px;height:30px;border-radius:50%;background:var(--white);display:flex;align-items:center;justify-content:center}
.topbar-right .item{display:flex;align-items:center;gap:14px;margin-right:34px}
.navbar{left:0;top:57px;width:1200px;height:85px;background:var(--white)}
.nav{position:absolute;top:96px;left:0;width:1200px;height:24px;font:500 16px 'Roboto',sans-serif;color:#222}
.nav span{position:absolute;top:0}
.nav .active{border-left:2px solid #222;padding-left:8px}
.logo-disc{left:138px;top:-18px;width:248px;height:248px;border-radius:50%;background:var(--white);z-index:3;display:flex;flex-direction:column;align-items:center;justify-content:flex-end;padding-bottom:48px}
.logo-disc .mark{width:70px;height:70px;border-radius:50%;background:var(--pale);margin-bottom:18px}
.logo-disc .name{font:500 21px 'Roboto',sans-serif;color:var(--blue)}
.hero{left:0;top:142px;width:1200px;height:800px;background:linear-gradient(180deg,#1e2733 0%,#384656 45%,#6b6258 70%,#2b3644 100%)}
.hero-title{left:0;top:320px;width:1200px;text-align:center;font:600 62px/70px 'Josefin Sans',sans-serif;color:var(--white)}
.dots{left:555px;top:697px;display:flex;gap:15px}
.dots i{width:12px;height:12px;border-radius:50%;background:var(--white);border:2px solid var(--white)}
.dots i.off{background:transparent}
.ghost{font:900 76px 'Roboto',sans-serif;color:var(--ghost);letter-spacing:1px;white-space:nowrap}
.heading{font:600 58px 'Josefin Sans',sans-serif;color:var(--blue);white-space:nowrap}
.heading em{font-style:normal;color:var(--grey)}
.about-brand{left:142px;top:957px;width:354px;height:443px;display:flex;align-items:center;justify-content:center;font:700 64px 'Roboto',sans-serif;color:var(--blue)}
.about-text{left:562px;top:1042px;width:493px;font-size:16px;line-height:29.6px;text-align:justify;color:#555}
.services-bg{left:0;top:1540px;width:1200px;height:832px;background:var(--pale)}
.card{position:absolute;background:var(--white);text-align:center}
.card h3{font:700 20px 'Roboto',sans-serif;color:#222;margin-bottom:14px}
.card p{font-size:14.5px;line-height:23px;color:#555;padding:0 30px}
.card .circle{position:absolute;border-radius:50%}
.arrow{width:42px;height:42px;border:2px solid #777;border-radius:50%;display:flex;align-items:center;justify-content:center}
.tile{position:absolute;border-radius:14px;overflow:hidden}
.play{left:731px;top:3039px;width:52px;height:52px;border-radius:50%;background:var(--white);display:flex;align-items:center;justify-content:center}
.frame{left:106px;top:3660px;width:266px;height:257px;border:4px solid var(--blue);border-radius:10px}
.contact-card{left:154px;top:3699px;width:892px;height:578px;background:var(--white);border-radius:14px;box-shadow:0 8px 30px rgba(0,0,0,.12)}
.field{position:absolute;border:1.5px solid #cfcfcf;font-size:15px;color:#444;padding:14px 20px}
.foot-info{font-size:14px;line-height:22px;color:var(--white)}
.foot-icon{width:42px;height:42px;border-radius:50%;border:1.5px solid #bbb;display:flex;align-items:center;justify-content:center}
.foot-nav{top:4428px;left:0;width:1200px;font:500 16px 'Roboto',sans-serif;color:var(--white)}
.foot-nav span{position:absolute}
.copyright{left:145px;top:4518px;font-size:13px;color:var(--white)}
.social{top:4510px;width:28px;height:28px;border-radius:50%;background:var(--white)}
</style>
</head>
<body>
<div class="page">

  <div class="abs topbar-left"></div>
  <div class="abs topbar-right">
    <div class="item"><span class="ico"><svg width="16" height="16" viewBox="0 0 24 24"><path fill="#24449c" d="M6.6 10.8a15 15 0 0 0 6.6 6.6l2.2-2.2c.3-.3.7-.4 1-.2 1.1.4 2.3.6 3.6.6.6 0 1 .4 1 1V20c0 .6-.4 1-1 1A17 17 0 0 1 3 4c0-.6.4-1 1-1h3.5c.6 0 1 .4 1 1 0 1.3.2 2.5.6 3.6.1.3 0 .7-.2 1z"/></svg></span>+91-9000012345</div>
    <div class="item"><span class="ico"><svg width="16" height="16" viewBox="0 0 24 24"><path fill="#24449c" d="M2 5h20v14H2z"/><path fill="none" stroke="#fff" stroke-width="2" d="M2 5l10 8 10-8"/></svg></span>mandporbex.team@mailbox.test</div>
  </div>
  <div class="abs navbar"></div>
  <nav class="nav">
    <span class="active" style="left:502px">HOME</span>
    <span style="left:601px">ABOUT US</span>
    <span style="left:723px">PRODUCTS</span>
    <span style="left:853px">OFFICE</span>
    <span style="left:950px">CONTACT US</span>
  </nav>
  <div class="abs logo-disc"><div class="mark"></div><div class="name">M and P Orbex</div></div>

  <div class="photo hero" role="img" aria-label="Warehouse aisle lined with stacked steel coils under a roof lit from the far end"></div>
  <h1 class="abs hero-title">The Perfect Fit For<br>Your Tube Bending Needs</h1>
  <div class="btn" style="left:510px;top:503px;width:181px;height:58px;border:2px solid #fff">Get Started</div>
  <div class="abs dots"><i></i><i class="off"></i><i></i><i></i></div>
  <svg class="abs" style="left:0;top:720px" width="1200" height="230" viewBox="0 0 1200 230">
    <path fill="#24449c" d="M0 120 C150 60 300 40 520 70 C760 105 900 150 1200 30 L1200 80 C950 190 760 150 560 130 C330 110 160 130 0 210 Z"/>
    <path fill="#ffffff" d="M0 230 L0 210 C160 130 330 110 560 130 C760 150 950 190 1200 80 L1200 230 Z"/>
  </svg>

  <div class="abs about-brand">M&amp;P Orbex</div>
  <div class="abs ghost" style="left:555px;top:906px">ABOUT US</div>
  <h2 class="abs heading" style="left:562px;top:950px">About <em>Us</em></h2>
  <p class="abs about-text">At M&amp;P Orbex, we specialize in precision tube bending and subassembly manufacturing, delivering expert solutions across a diverse range of materials including mild steel, stainless steel, aluminum, and other non-ferrous metals. We partner closely with our clients to engineer precise components that meet exacting industry standards. Whether your project requires small-batch prototyping or high-volume production runs, our experienced engineering team works efficiently to enhance product quality, streamline manufacturing processes, and reduce overall costs. "We provide complete solutions for your complex challenges.</p>
  <div class="btn" style="left:562px;top:1373px;width:147px;height:50px">Read More</div>

  <svg class="abs" style="left:0;top:1390px" width="1200" height="160" viewBox="0 0 1200 160">
    <path fill="#e1e9f8" d="M0 160 L0 120 C120 60 250 40 420 70 C620 110 820 140 1000 90 C1100 60 1160 30 1200 10 L1200 160 Z"/>
    <path fill="none" stroke="#c9d5ee" stroke-width="10" d="M110 60 C300 20 520 70 700 100 C880 130 1060 110 1200 0"/>
    <path fill="none" stroke="#c9d5ee" stroke-width="5" d="M520 90 C700 130 900 140 1200 40"/>
  </svg>
  <div class="abs services-bg"></div>
  <div class="abs ghost" style="left:32px;top:1650px;color:var(--ghost-blue)">SERVICES</div>
  <h2 class="abs heading" style="left:427px;top:1668px">Our <em>Services</em></h2>

  <div class="abs arrow" style="left:71px;top:2003px"><svg width="16" height="16" viewBox="0 0 16 16"><path d="M10 2 L4 8 L10 14" fill="none" stroke="#555" stroke-width="2"/></svg></div>
  <div class="abs arrow" style="left:1085px;top:2003px"><svg width="16" height="16" viewBox="0 0 16 16"><path d="M6 2 L12 8 L6 14" fill="none" stroke="#555" stroke-width="2"/></svg></div>

  <div class="card" style="left:145px;top:1785px;width:289px;height:480px;border-radius:145px 145px 0 0">
    <div class="circle" role="img" aria-label="Bent stainless steel tubes" style="left:42px;top:14px;width:205px;height:205px;background:radial-gradient(circle,#9aa3ac,#4a525c)"></div>
    <div style="position:absolute;top:240px;width:100%"><h3>Tube and Pipe Bending</h3><p>We specialize in Tube and Pipe Bending We handle a variety of industrial projects with a wide scope of customer needs.</p></div>
    <div class="btn" style="left:70px;top:393px;width:150px;height:50px">Read More</div>
  </div>
  <div class="card" style="left:455px;top:1785px;width:289px;height:490px;border-radius:0 0 145px 145px;border-bottom:5px solid var(--blue)">
    <div style="position:absolute;top:30px;width:100%"><h3>Tube End Forming</h3><p>Our tube end forming service is second to none, providing precision and customization for all your project needs.</p></div>
    <div class="btn" style="left:70px;top:183px;width:150px;height:50px">Read More</div>
    <div class="circle" role="img" aria-label="Formed tube ends and fittings" style="left:40px;top:258px;width:210px;height:210px;border:1px solid #9fb0d8;background:radial-gradient(circle,#ffffff 55%,#e3e6ea)"></div>
  </div>
  <div class="card" style="left:766px;top:1785px;width:289px;height:480px;border-radius:145px 145px 0 0">
    <div class="circle" role="img" aria-label="Insulated exhaust pipe section" style="left:42px;top:14px;width:205px;height:205px;background:radial-gradient(circle,#c9c3b8,#e6e6e6)"></div>
    <div style="position:absolute;top:240px;width:100%"><h3>Thermal Insulation</h3><p>We offer comprehensive automotive insulation solutions, including Thermal Insulation for exhaust pipes.</p></div>
    <div class="btn" style="left:70px;top:393px;width:150px;height:50px">Read More</div>
  </div>

  <div class="abs ghost" style="left:245px;top:2470px">PROJECT GALLERY</div>
  <h2 class="abs heading" style="left:398px;top:2490px">Project <em>Gallery</em></h2>
  <div class="tile" role="img" aria-label="Tube bending die on machine" style="left:145px;top:2618px;width:298px;height:291px;background:linear-gradient(135deg,#cfc7b8,#6e6458)"></div>
  <div class="tile" role="img" aria-label="Bent tube on a press" style="left:452px;top:2618px;width:298px;height:291px;background:linear-gradient(135deg,#8a8a8a,#2e2e2e)"></div>
  <div class="tile" role="img" aria-label="Engineers reviewing plans on the factory floor" style="left:757px;top:2618px;width:298px;height:291px;background:linear-gradient(135deg,#5d6b80,#b59a3c)"></div>
  <div class="tile" role="img" aria-label="Roller dies of a bending machine" style="left:145px;top:2918px;width:298px;height:290px;background:linear-gradient(135deg,#bdb9b2,#4b4a48)"></div>
  <div class="tile" role="img" aria-label="Video of workers inspecting the production line" style="left:452px;top:2918px;width:603px;height:290px;background:linear-gradient(135deg,#3552a8,#24449c)"></div>
  <div class="abs play"><svg width="18" height="20" viewBox="0 0 18 20"><path d="M2 1 L17 10 L2 19 Z" fill="#24449c"/></svg></div>
  <div class="tile" role="img" aria-label="CNC tube bender forming a steel tube" style="left:145px;top:3217px;width:605px;height:291px;background:linear-gradient(90deg,#c8ccd2,#7d6f6c 60%,#a43c30)"></div>
  <div class="tile" role="img" aria-label="Bending wheel and rollers" style="left:757px;top:3217px;width:298px;height:291px;background:linear-gradient(135deg,#6e6e6e,#2a2a2a)"></div>
  <div class="btn" style="left:525px;top:3552px;width:150px;height:48px">View More</div>

  <svg class="abs" style="left:0;top:3880px" width="1200" height="683" viewBox="0 0 1200 683">
    <path fill="#4e4e4e" d="M0 220 C180 90 420 70 700 110 C900 140 1080 90 1200 20 L1200 683 L0 683 Z"/>
    <path fill="#24449c" d="M1030 150 C1100 120 1160 70 1200 30 L1200 0 C1150 50 1090 100 1030 130 Z"/>
  </svg>
  <div class="abs frame"></div>
  <div class="abs contact-card"></div>
  <div class="photo" role="img" aria-label="Coiled chrome tube" style="left:154px;top:3699px;width:262px;height:175px;border-radius:14px 0 0 0;background:radial-gradient(circle at 40% 50%,#d8d8d8,#ffffff 70%)"></div>
  <div class="photo" role="img" aria-label="Plumber fitting a pipe with a wrench" style="left:798px;top:4112px;width:248px;height:165px;border-radius:0 0 14px 0;background:linear-gradient(135deg,#ffffff,#cfd5de 60%,#b7a08a)"></div>
  <div class="abs ghost" style="left:204px;top:4155px">CONTACT</div>
  <h2 class="abs heading" style="left:450px;top:3770px">Contact <em>Us</em></h2>
  <div class="field" style="left:234px;top:3875px;width:358px;height:49px">First Name</div>
  <div class="field" style="left:606px;top:3875px;width:358px;height:49px">Last Name</div>
  <div class="field" style="left:234px;top:3940px;width:358px;height:50px">Email address</div>
  <div class="field" style="left:606px;top:3940px;width:358px;height:50px">Phone Number</div>
  <div class="field" style="left:234px;top:4006px;width:730px;height:110px">Message</div>
  <div class="btn" style="left:525px;top:4149px;width:150px;height:48px">Submit</div>

  <div class="abs foot-icon" style="left:209px;top:4336px"><svg width="14" height="18" viewBox="0 0 14 18"><path fill="#fff" d="M7 0a7 7 0 0 0-7 7c0 5 7 11 7 11s7-6 7-11a7 7 0 0 0-7-7zm0 9.5A2.5 2.5 0 1 1 7 4.5a2.5 2.5 0 0 1 0 5z"/></svg></div>
  <div class="abs foot-info" style="left:270px;top:4335px">P12 'K' Block Udyog Nagar<br>Pune- 411000, India</div>
  <div class="abs foot-icon" style="left:500px;top:4336px;background:var(--blue);border-color:var(--blue)"><svg width="16" height="16" viewBox="0 0 24 24"><path fill="#fff" d="M6.6 10.8a15 15 0 0 0 6.6 6.6l2.2-2.2c.3-.3.7-.4 1-.2 1.1.4 2.3.6 3.6.6.6 0 1 .4 1 1V20c0 .6-.4 1-1 1A17 17 0 0 1 3 4c0-.6.4-1 1-1h3.5c.6 0 1 .4 1 1 0 1.3.2 2.5.6 3.6.1.3 0 .7-.2 1z"/></svg></div>
  <div class="abs" style="left:560px;top:4346px;font:500 18px 'Roboto',sans-serif;color:#fff">+91-9000012345</div>
  <div class="abs foot-icon" style="left:741px;top:4336px"><svg width="16" height="14" viewBox="0 0 24 20"><path fill="#fff" d="M1 2h22v16H1z"/><path fill="none" stroke="#4e4e4e" stroke-width="2" d="M1 2l11 8 11-8"/></svg></div>
  <div class="abs foot-info" style="left:803px;top:4346px">mandporbex.team@mailbox.test</div>
  <nav class="abs foot-nav">
    <span style="left:339px">HOME</span>
    <span style="left:424px">ABOUT US</span>
    <span style="left:542px">PRODUCTS</span>
    <span style="left:666px">OFFICE</span>
    <span style="left:759px">CONTACT US</span>
  </nav>
  <div class="abs copyright">Copyrights © 2026, Companyname. All Rights Reserved &nbsp;|&nbsp; Privacy Policy &nbsp;|&nbsp; Terms and Conditions</div>
  <div class="abs social" style="left:918px"></div>
  <div class="abs social" style="left:954px"></div>
  <div class="abs social" style="left:989px"></div>
  <div class="abs social" style="left:1026px"></div>
</div>
</body>
</html>
```